Bref créative
TRV Construction Supplies Stationary Package
Complete Stationary Package, Biz Cards, Letterhead, Folder, Comp Slips
Professional
Owen Pellig
Marketing Executive
Unit K
Ridgefield Distribution Centre
Harcombe Way
Avonmouth
Bristol
BS10 4QJ
owenpellig@tumblingkite.co.uk
www.trvcs.co.uk
Would like options using either of the backgrounds we have provided.....
Would like the back of our business card to use the black background logo.

```html
<!DOCTYPE html>
<html lang="en">
<head>
<meta charset="utf-8">
<title>TRV Construction Supplies – Stationery Package</title>
<link href="https://fonts.googleapis.com/css2?family=Montserrat:wght@400;600;800&family=Great+Vibes&display=swap" rel="stylesheet">
<style>
  :root{
    --bg:#ece7e1;
    --paper:#ffffff;
    --ink:#231f20;
    --grey:#8c8c8c;
    --grey-light:#d9d9d9;
    --orange:#f5a021;
    --orange-deep:#e4661a;
    --shadow:0 3px 8px rgba(0,0,0,.18);
  }
  *{box-sizing:border-box;margin:0;padding:0}
  html,body{width:1200px;height:497px;overflow:hidden}
  body{background:var(--bg);font-family:"Montserrat",Arial,sans-serif;color:var(--ink);position:relative}
  .piece{position:absolute;background:var(--paper);box-shadow:var(--shadow);overflow:hidden}
  .piece svg.shape{position:absolute;inset:0;width:100%;height:100%}

  /* company name lockup */
  .lockup{position:absolute;display:flex;align-items:center;gap:4px;font-weight:800;color:var(--ink);line-height:1}
  .lockup .dot{width:9px;height:9px;background:var(--orange)}
  .lockup .name{display:flex;flex-direction:column}
  .lockup .big{font-size:15px;letter-spacing:.5px}
  .lockup .small{font-size:5.5px;letter-spacing:.3px;margin-top:1px}
  .lockup.on-dark{color:#fff}
  .lockup.on-orange .dot{background:var(--ink)}

  .details{position:absolute;font-size:5px;line-height:1.45;color:var(--ink)}
  .details.on-dark{color:#fff}
  .details strong{font-weight:600;font-size:6px;display:block}

  /* business cards */
  .card{width:126px;height:110px;border-radius:3px}
  .card-front-white{left:20px;top:50px}
  .card-front-black{left:152px;top:50px;background:var(--ink)}
  .card-back-white{left:20px;top:176px}
  .card-back-orange{left:152px;top:176px;background:linear-gradient(135deg,var(--orange) 0%,var(--orange-deep) 100%)}

  /* compliment slip */
  .comp-slip{left:28px;top:300px;width:262px;height:138px}
  .comp-slip .greeting{position:absolute;left:46px;top:82px;font-family:"Great Vibes",cursive;font-size:30px;color:var(--orange)}

  /* letterhead */
  .letterhead{left:392px;top:20px;width:190px;height:436px}

  /* envelopes */
  .envelope-open{left:708px;top:24px;width:262px;height:150px;background:transparent;box-shadow:none;overflow:visible}
  .envelope-plain{left:740px;top:132px;width:245px;height:118px}
  .envelope-front{left:612px;top:238px;width:218px;height:206px}
</style>
</head>
<body>

<!-- Business card: front, white -->
<section class="piece card card-front-white" aria-label="Business card front">
  <svg class="shape" viewBox="0 0 126 110" preserveAspectRatio="none">
    <path d="M0 0 H34 C18 30 16 70 30 110 H0 Z" fill="var(--orange)"/>
    <path d="M0 0 H24 C10 30 8 70 20 110 H0 Z" fill="var(--orange-deep)"/>
  </svg>
  <div class="lockup" style="left:42px;top:14px">
    <span class="dot"></span>
    <span class="name"><span class="big">TRV</span><span class="small">CONSTRUCTION<br>SUPPLIES</span></span>
  </div>
  <div class="details" style="left:40px;top:60px">
    <strong>Owen Pellig</strong>
    Marketing Executive<br>
    T: 0117 496 0321<br>
    owenpellig@tumblingkite.co.uk
  </div>
</section>

<!-- Business card: front, black -->
<section class="piece card card-front-black" aria-label="Business card front, dark">
  <svg class="shape" viewBox="0 0 126 110" preserveAspectRatio="none">
    <path d="M126 40 C104 60 96 88 100 110 H126 Z" fill="var(--orange)"/>
    <path d="M126 55 C112 70 106 92 110 110 H126 Z" fill="var(--orange-deep)"/>
  </svg>
  <div class="lockup on-dark" style="left:12px;top:14px">
    <span class="dot"></span>
    <span class="name"><span class="big">TRV</span><span class="small">CONSTRUCTION<br>SUPPLIES</span></span>
  </div>
  <div class="details on-dark" style="left:12px;top:60px">
    <strong>Owen Pellig</strong>
    Marketing Executive<br>
    M: 07700 900417<br>
    owenpellig@tumblingkite.co.uk
  </div>
</section>

<!-- Business card: back, white -->
<section class="piece card card-back-white" aria-label="Business card back">
  <svg class="shape" viewBox="0 0 126 110" preserveAspectRatio="none">
    <path d="M0 92 C40 80 90 84 126 70 V110 H0 Z" fill="var(--orange)"/>
    <path d="M0 100 C40 92 90 94 126 84 V110 H0 Z" fill="var(--orange-deep)"/>
  </svg>
  <div class="lockup" style="left:26px;top:30px">
    <span class="dot"></span>
    <span class="name"><span class="big">TRV</span><span class="small">CONSTRUCTION<br>SUPPLIES</span></span>
  </div>
  <div class="details" style="left:44px;top:72px">www.trvcs.co.uk</div>
</section>

<!-- Business card: back, orange -->
<section class="piece card card-back-orange" aria-label="Business card back, orange">
  <div class="lockup on-orange" style="left:26px;top:36px">
    <span class="dot"></span>
    <span class="name"><span class="big">TRV</span><span class="small">CONSTRUCTION<br>SUPPLIES</span></span>
  </div>
</section>

<!-- Compliment slip -->
<section class="piece comp-slip" aria-label="Compliment slip">
  <svg class="shape" viewBox="0 0 262 138" preserveAspectRatio="none">
    <path d="M262 0 V60 C246 40 236 20 232 0 Z" fill="var(--orange)"/>
    <path d="M262 0 V36 C254 24 248 12 246 0 Z" fill="var(--orange-deep)"/>
    <path d="M0 128 C80 114 180 116 262 104" stroke="var(--grey-light)" stroke-width="1" fill="none"/>
  </svg>
  <div class="lockup" style="left:14px;top:14px">
    <span class="dot"></span>
    <span class="name"><span class="big">TRV</span><span class="small">CONSTRUCTION<br>SUPPLIES</span></span>
  </div>
  <div class="details" style="left:150px;top:14px">
    Unit K, Ridgefield Distribution Centre<br>
    Harcombe Way, Avonmouth<br>
    Bristol BS10 4QJ<br>
    T: 0117 496 0321<br>
    www.trvcs.co.uk
  </div>
  <p class="greeting">With compliments</p>
</section>

<!-- Letterhead -->
<section class="piece letterhead" aria-label="Letterhead">
  <svg class="shape" viewBox="0 0 190 436" preserveAspectRatio="none">
    <path d="M0 56 C60 44 130 46 190 36" stroke="var(--grey-light)" stroke-width="1" fill="none"/>
    <path d="M0 420 C60 408 130 410 190 398" stroke="var(--grey-light)" stroke-width="1" fill="none"/>
  </svg>
  <div class="lockup" style="left:12px;top:10px">
    <span class="dot"></span>
    <span class="name"><span class="big">TRV</span><span class="small">CONSTRUCTION<br>SUPPLIES</span></span>
  </div>
  <div class="details" style="left:104px;top:8px">
    Unit K<br>
    Ridgefield Distribution Centre<br>
    Harcombe Way<br>
    Avonmouth<br>
    Bristol<br>
    BS10 4QJ<br>
    T: 0117 496 0321<br>
    F: 0117 496 0322<br>
    www.trvcs.co.uk
  </div>
</section>

<!-- Envelope, open flap -->
<section class="piece envelope-open" aria-label="Envelope, back with open flap">
  <svg class="shape" viewBox="0 0 262 150" preserveAspectRatio="none" style="filter:drop-shadow(0 3px 4px rgba(0,0,0,.18))">
    <path d="M0 50 L131 0 L262 50 Z" fill="#9a9a9a"/>
    <path d="M12 50 L131 8 L250 50 Z" fill="#7d7d7d"/>
    <rect x="0" y="50" width="262" height="100" fill="var(--paper)"/>
    <path d="M0 50 L131 110 L262 50" stroke="var(--grey-light)" stroke-width="1" fill="none"/>
  </svg>
</section>

<!-- Envelope, plain front -->
<section class="piece envelope-plain" aria-label="Envelope, front">
  <div class="lockup" style="left:12px;top:10px">
    <span class="dot"></span>
    <span class="name"><span class="big">TRV</span><span class="small">CONSTRUCTION<br>SUPPLIES</span></span>
  </div>
</section>

<!-- Envelope, orange flap -->
<section class="piece envelope-front" aria-label="Envelope with orange flap">
  <svg class="shape" viewBox="0 0 218 206" preserveAspectRatio="none">
    <defs>
      <linearGradient id="flapGradient" x1="0" y1="0" x2="1" y2="1">
        <stop offset="0" stop-color="var(--orange)"/>
        <stop offset="1" stop-color="var(--orange-deep)"/>
      </linearGradient>
    </defs>
    <path d="M0 0 H218 V70 C150 40 70 40 0 90 Z" fill="url(#flapGradient)"/>
    <path d="M0 90 C70 40 150 40 218 70" stroke="#fff" stroke-width="2" fill="none"/>
  </svg>
  <div class="lockup" style="left:12px;top:92px">
    <span class="dot"></span>
    <span class="name"><span class="big">TRV</span><span class="small">CONSTRUCTION<br>SUPPLIES</span></span>
  </div>
  <div class="details" style="left:12px;top:134px">
    Unit K, Ridgefield Distribution Centre<br>
    Harcombe Way, Avonmouth<br>
    Bristol BS10 4QJ<br>
    www.trvcs.co.uk
  </div>
</section>

</body>
</html>
```